Manufacturer's Representative Group needs a clean new Website

We represent and sell a number of suppliers that design and build products used in Biopharmaceutical manufacturing. Our sales region is in the central US. Our customer base is scientific / engineering based - so clean, we organized design with a focus on the products - easy and clear navigation is necessary. We do not sell direct or warehouse product - so e-commerce is not needed. Our customers will use the website for reference on what we do and offer - we will use the site as a platform to present products from each vendor and the home page will be used to capture an overview and draw users deeper into the site. You can view our current site - which needs A LOT of help to get ideas on products represented and types of products

Target Market(s)

Engineers and Pharmaceutical / Bio pharm end users

Industry/Entity Type

E-Commerce

Number of Pages Required

2 page

Font styles to use
Sans Serif

Requirements
Must have
• I need a home page that provides a snapshot of my company and the product lines we represent - then a second page that I can copy as a template for each line I rep as well as for an "About us / contact" page.
• I would like to be able to manage content on the pages so something easy to adjust pictures or add content is a must
• Must use our logo

```html
<!DOCTYPE html>
<html lang="en">
<head>
<meta charset="utf-8">
<title>Prairie Bio</title>
<link href="https://fonts.googleapis.com/css2?family=Open+Sans:wght@300;400;600;700;800&display=swap" rel="stylesheet">
<style>
:root{
  --orange:#e8623a;
  --ink:#3b3b3b;
  --muted:#8a8a8a;
  --line:#d6d6d6;
  --paper:#ffffff;
  --panel:#f4f4f4;
  --about:#e2e1df;
  --footer:#2f2f2f;
  --footer-deep:#232323;
  --tile-dark:#3f3f3f;
}
*{box-sizing:border-box;margin:0;padding:0}
html,body{width:1200px;height:2438px;overflow:hidden}
body{font-family:"Open Sans",Arial,sans-serif;color:var(--ink);background:var(--paper);position:relative}
.abs{position:absolute}

/* header */
.site-header{position:absolute;left:0;top:0;width:1200px;height:81px;background:var(--paper)}
.brand{position:absolute;left:88px;top:22px;display:flex;align-items:center;gap:10px;font-size:30px;font-weight:600;color:var(--ink)}
.brand-dot{width:26px;height:26px;border-radius:50%;background:var(--orange)}
.main-nav{position:absolute;right:86px;top:22px;display:flex}
.main-nav a{font-size:16px;font-weight:600;color:var(--ink);text-decoration:none;padding:9px 18px;border-left:1px solid var(--line)}
.main-nav a:first-child{border-left:none}
.main-nav a.active{background:var(--orange);color:#fff}

/* hero */
.hero{position:absolute;left:0;top:81px;width:1200px;height:420px;
  background:radial-gradient(circle at 25% 40%,#5c6a4c 0,#2f3a34 30%,#1c2228 60%),#1c2228;overflow:hidden}
.hero-photo{position:absolute;left:820px;top:20px;width:260px;height:380px;
  background:radial-gradient(ellipse at 50% 75%,#3f9a7a 0,#5a7f77 35%,rgba(120,140,140,.25) 60%,transparent 72%)}
.hero-rule{position:absolute;left:168px;top:122px;width:3px;height:170px;background:#fff}
.hero-kicker{position:absolute;left:182px;top:114px;font-size:46px;font-weight:300;color:#fff;letter-spacing:1px}
.hero-title{position:absolute;left:180px;top:160px;font-size:62px;font-weight:800;color:#fff;letter-spacing:1px}
.hero-lede{position:absolute;left:182px;top:245px;font-size:16px;font-weight:700;color:#fff;line-height:24px}
.hero-more{position:absolute;left:172px;top:293px;background:#fff;color:var(--ink);font-size:12px;font-weight:700;padding:4px 12px}
.hero-arrow{position:absolute;top:170px}

/* featured slide */
.feature-card{position:absolute;left:89px;top:550px;width:447px;height:236px;background:#fff;box-shadow:0 3px 10px rgba(0,0,0,.25);overflow:hidden}
.feature-photo{position:absolute;left:0;top:0;width:204px;height:236px;background:linear-gradient(160deg,#e9eef2,#c9d3da)}
.feature-body{position:absolute;left:228px;top:16px;width:200px}
.feature-label{font-size:10px;color:var(--muted);font-weight:600}
.feature-title{font-size:14px;font-weight:700;color:var(--orange);margin-bottom:6px}
.feature-text{font-size:9.5px;line-height:15px;color:#555}
.feature-btn{position:absolute;right:14px;bottom:12px;background:var(--orange);color:#fff;font-size:11px;padding:4px 10px}
.feature-ribbon{position:absolute;right:0;top:0}
.slider-dots{position:absolute;left:492px;top:826px;display:flex;gap:5px}
.slider-dots span{width:10px;height:10px;border-radius:50%;background:#555}
.slider-dots span.on{background:#aaa}

/* companies */
.section-title{font-weight:300;color:var(--ink)}
.companies-title{position:absolute;left:612px;top:540px;font-size:31px}
.companies-rule{position:absolute;left:602px;top:592px;width:498px;height:1px;background:var(--line)}
.company-grid{position:absolute;left:600px;top:612px;width:500px;display:grid;grid-template-columns:repeat(3,1fr);row-gap:22px}
.company{height:68px;display:flex;align-items:center;justify-content:center;font-size:19px;font-weight:600;color:#6d6d6d}

/* products */
.products-title{position:absolute;left:87px;top:872px;font-size:34px}
.products-rule{position:absolute;left:87px;top:936px;width:1011px;height:1px;background:var(--line)}
.product{position:absolute;width:236px;height:317px;background:#fff;border:1px solid var(--line)}
.product-photo{height:233px;border-bottom:4px solid var(--orange);position:relative}
.photo-light{background:linear-gradient(150deg,#eeeeee,#c8c8c8)}
.photo-dark{background:radial-gradient(circle at 50% 50%,#5a5a5a,var(--tile-dark))}
.tile-actions{position:absolute;left:80px;top:96px;display:flex;gap:6px}
.tile-actions span{width:34px;height:34px;display:flex;align-items:center;justify-content:center}
.act-share{background:#fff}
.act-like{background:var(--orange)}
.product-name{position:absolute;left:14px;top:248px;font-size:14px;color:#555}
.product-cat{position:absolute;left:14px;top:272px;font-size:10px;font-weight:700;color:var(--orange)}
.product-link{position:absolute;right:12px;top:250px;width:38px;height:38px;border-radius:50%;background:var(--orange);display:flex;align-items:center;justify-content:center}

/* sidebar */
.sidebar{position:absolute;left:872px;top:992px;width:236px;height:674px;background:var(--panel);border:1px solid var(--line)}
.side-title{position:absolute;left:12px;font-size:18px;font-weight:400;color:var(--ink)}
.side-rule{position:absolute;left:12px;width:210px;height:1px;background:var(--line)}
.field-label{position:absolute;left:14px;font-size:11px;color:#444}
.field{position:absolute;left:14px;width:206px;height:20px;background:#fff;border:1px solid #e3e3e3}
.submit{position:absolute;left:14px;top:276px;width:206px;height:22px;background:var(--orange);color:#fff;font-size:11px;font-weight:700;text-align:center;line-height:22px}
.person{position:absolute;left:12px;width:212px;height:120px}
.person-photo{position:absolute;left:0;top:0;width:68px;height:80px;background:linear-gradient(#bdb6ae,#8c857e)}
.person-name{position:absolute;left:78px;top:0;font-size:19px;color:var(--ink)}
.person-info{position:absolute;left:78px;top:30px;font-size:8px;line-height:12px;color:#666;width:134px}
.person-social{position:absolute;left:4px;top:88px;display:flex;gap:8px}
.person-social span{width:9px;height:9px;border-radius:50%;background:#555}

/* about */
.about{position:absolute;left:0;top:1728px;width:1200px;height:447px;background:var(--about);overflow:hidden}
.about-photo{position:absolute;left:677px;top:0;width:523px;height:447px;
  background:linear-gradient(120deg,rgba(226,225,223,1) 0,rgba(226,225,223,0) 25%),linear-gradient(135deg,#f4f4f4,#bdbdbd 55%,#8e8e8e)}
.about-title{position:absolute;left:89px;top:58px;font-size:36px}
.about-text{position:absolute;left:89px;top:136px;width:700px;font-size:14px;line-height:27px;color:#444}

/* footer */
.site-footer{position:absolute;left:0;top:2175px;width:1200px;height:195px;background:var(--footer)}
.footer-title{position:absolute;left:89px;top:38px;font-size:18px;color:#7a7a7a}
.footer-info{position:absolute;left:89px;top:66px;font-size:12px;line-height:17px;color:#6b6b6b}
.to-top{position:absolute;left:1037px;top:33px;width:73px;height:68px;border:2px solid #fff;display:flex;align-items:center;justify-content:center}
.copyright{position:absolute;right:92px;top:132px;font-size:14px;color:#cfcfcf}
.footer-bar{position:absolute;left:0;top:2370px;width:1200px;height:68px;background:var(--footer-deep)}
.footer-social{position:absolute;right:90px;top:28px;display:flex;gap:12px}
.footer-social span{width:14px;height:14px;border-radius:50%;background:#fff}
</style>
</head>
<body>

<header class="site-header">
  <div class="brand"><span class="brand-dot"></span>Prairie Bio</div>
  <nav class="main-nav">
    <a href="#">HOME</a><a href="#">ABOUT</a><a href="#" class="active">PAGES</a><a href="#">CAREER</a><a href="#">CONTACT</a>
  </nav>
</header>

<section class="hero">
  <div class="hero-photo" role="img" aria-label="Glass laboratory flask with green liquid"></div>
  <div class="hero-rule"></div>
  <div class="hero-kicker">CERTIFIED CLEAN</div>
  <div class="hero-title">PHARMAVESSELS</div>
  <div class="hero-lede">LOREM IPSUM DOLOR SIT AMET, CONSECTETUR ADIPIS<br>VESTIBULUM SCELERISQUE IN ENIM</div>
  <div class="hero-more">MORE</div>
  <svg class="hero-arrow" style="left:88px" width="20" height="44" viewBox="0 0 20 44"><path d="M18 2 2 22l16 20" fill="none" stroke="#fff" stroke-width="2.5"/></svg>
  <svg class="hero-arrow" style="left:1092px" width="20" height="44" viewBox="0 0 20 44"><path d="M2 2l16 20L2 42" fill="none" stroke="#fff" stroke-width="2.5"/></svg>
</section>

<article class="feature-card">
  <div class="feature-photo" role="img" aria-label="Sterile plastic bottles with tubing assemblies"></div>
  <div class="feature-body">
    <div class="feature-label">LATEST</div>
    <div class="feature-title">HALDEN WORKS</div>
    <p class="feature-text">Single-use bottle sets for clean fill work. Sealed tubing keeps media safe. Each set ships ready for gamma treatment. Caps fit standard lines. Sizes range widely. Ask your rep for sample kits and lead times in your area today.</p>
  </div>
  <div class="feature-btn">Read more</div>
  <svg class="feature-ribbon" width="60" height="60" viewBox="0 0 60 60"><path d="M10 0h18l32 32v18z" fill="var(--orange)"/></svg>
</article>
<div class="slider-dots"><span></span><span></span><span></span><span class="on"></span></div>

<h2 class="section-title companies-title">COMPANIES REPRESENTED</h2>
<div class="companies-rule"></div>
<div class="company-grid">
  <div class="company">Ardent Hose Co.</div>
  <div class="company">PureSeal</div>
  <div class="company">Ardent Hose Co.</div>
  <div class="company">Veritune</div>
  <div class="company">Tarlow Pumps</div>
  <div class="company">Veritune</div>
  <div class="company">Norvane Polymers</div>
  <div class="company">Q-Form Systems</div>
  <div class="company">Norvane Polymers</div>
</div>

<h2 class="section-title products-title">PRODUCTS</h2>
<div class="products-rule"></div>

<article class="product" style="left:89px;top:992px">
  <div class="product-photo photo-light" role="img" aria-label="Stainless steel washer unit"></div>
  <div class="product-name">Skater Dress In Leaf</div><div class="product-cat">Women / Clothe</div>
  <div class="product-link"><svg width="18" height="18" viewBox="0 0 18 18"><path d="M7 11l4-4M8 4l2-2a3 3 0 0 1 4 4l-2 2M10 14l-2 2a3 3 0 0 1-4-4l2-2" fill="none" stroke="#fff" stroke-width="2"/></svg></div>
</article>
<article class="product" style="left:347px;top:992px">
  <div class="product-photo photo-light" role="img" aria-label="Flexible metal bellows fitting"></div>
  <div class="product-name">Pipe &amp; Tube Fittings</div><div class="product-cat">Women / Clothe</div>
  <div class="product-link"><svg width="18" height="18" viewBox="0 0 18 18"><path d="M7 11l4-4M8 4l2-2a3 3 0 0 1 4 4l-2 2M10 14l-2 2a3 3 0 0 1-4-4l2-2" fill="none" stroke="#fff" stroke-width="2"/></svg></div>
</article>
<article class="product" style="left:610px;top:992px">
  <div class="product-photo photo-dark" role="img" aria-label="Product photo">
    <div class="tile-actions">
      <span class="act-share"><svg width="16" height="16" viewBox="0 0 16 16"><circle cx="12" cy="3" r="2.3" fill="var(--orange)"/><circle cx="4" cy="8" r="2.3" fill="var(--orange)"/><circle cx="12" cy="13" r="2.3" fill="var(--orange)"/><path d="M12 3 4 8l8 5" fill="none" stroke="var(--orange)" stroke-width="1.5"/></svg></span>
      <span class="act-like"><svg width="16" height="16" viewBox="0 0 16 16"><path d="M1 7h3v8H1zM5 7l3-6c1.5 0 2 1 1.6 2.5L9 6h5a1.5 1.5 0 0 1 1.4 2l-2 6a1.5 1.5 0 0 1-1.4 1H5z" fill="#fff"/></svg></span>
    </div>
  </div>
  <div class="product-name">Skater Dress In Leaf</div><div class="product-cat">Women / Clothe</div>
  <div class="product-link"><svg width="18" height="18" viewBox="0 0 18 18"><path d="M7 11l4-4M8 4l2-2a3 3 0 0 1 4 4l-2 2M10 14l-2 2a3 3 0 0 1-4-4l2-2" fill="none" stroke="#fff" stroke-width="2"/></svg></div>
</article>

<article class="product" style="left:89px;top:1352px">
  <div class="product-photo photo-dark" role="img" aria-label="Product photo">
    <div class="tile-actions">
      <span class="act-share"><svg width="16" height="16" viewBox="0 0 16 16"><circle cx="12" cy="3" r="2.3" fill="var(--orange)"/><circle cx="4" cy="8" r="2.3" fill="var(--orange)"/><circle cx="12" cy="13" r="2.3" fill="var(--orange)"/><path d="M12 3 4 8l8 5" fill="none" stroke="var(--orange)" stroke-width="1.5"/></svg></span>
      <span class="act-like"><svg width="16" height="16" viewBox="0 0 16 16"><path d="M1 7h3v8H1zM5 7l3-6c1.5 0 2 1 1.6 2.5L9 6h5a1.5 1.5 0 0 1 1.4 2l-2 6a1.5 1.5 0 0 1-1.4 1H5z" fill="#fff"/></svg></span>
    </div>
  </div>
  <div class="product-name">Skater Dress In Leaf</div><div class="product-cat">Women / Clothe</div>
  <div class="product-link"><svg width="18" height="18" viewBox="0 0 18 18"><path d="M7 11l4-4M8 4l2-2a3 3 0 0 1 4 4l-2 2M10 14l-2 2a3 3 0 0 1-4-4l2-2" fill="none" stroke="#fff" stroke-width="2"/></svg></div>
</article>
<article class="product" style="left:347px;top:1352px">
  <div class="product-photo photo-dark" role="img" aria-label="Product photo">
    <div class="tile-actions">
      <span class="act-share"><svg width="16" height="16" viewBox="0 0 16 16"><circle cx="12" cy="3" r="2.3" fill="var(--orange)"/><circle cx="4" cy="8" r="2.3" fill="var(--orange)"/><circle cx="12" cy="13" r="2.3" fill="var(--orange)"/><path d="M12 3 4 8l8 5" fill="none" stroke="var(--orange)" stroke-width="1.5"/></svg></span>
      <span class="act-like"><svg width="16" height="16" viewBox="0 0 16 16"><path d="M1 7h3v8H1zM5 7l3-6c1.5 0 2 1 1.6 2.5L9 6h5a1.5 1.5 0 0 1 1.4 2l-2 6a1.5 1.5 0 0 1-1.4 1H5z" fill="#fff"/></svg></span>
    </div>
  </div>
  <div class="product-name">Skater Dress In Leaf</div><div class="product-cat">Women / Clothe</div>
  <div class="product-link"><svg width="18" height="18" viewBox="0 0 18 18"><path d="M7 11l4-4M8 4l2-2a3 3 0 0 1 4 4l-2 2M10 14l-2 2a3 3 0 0 1-4-4l2-2" fill="none" stroke="#fff" stroke-width="2"/></svg></div>
</article>
<article class="product" style="left:610px;top:1352px">
  <div class="product-photo photo-dark" role="img" aria-label="Product photo">
    <div class="tile-actions">
      <span class="act-share"><svg width="16" height="16" viewBox="0 0 16 16"><circle cx="12" cy="3" r="2.3" fill="var(--orange)"/><circle cx="4" cy="8" r="2.3" fill="var(--orange)"/><circle cx="12" cy="13" r="2.3" fill="var(--orange)"/><path d="M12 3 4 8l8 5" fill="none" stroke="var(--orange)" stroke-width="1.5"/></svg></span>
      <span class="act-like"><svg width="16" height="16" viewBox="0 0 16 16"><path d="M1 7h3v8H1zM5 7l3-6c1.5 0 2 1 1.6 2.5L9 6h5a1.5 1.5 0 0 1 1.4 2l-2 6a1.5 1.5 0 0 1-1.4 1H5z" fill="#fff"/></svg></span>
    </div>
  </div>
  <div class="product-name">Skater Dress In Leaf</div><div class="product-cat">Women / Clothe</div>
  <div class="product-link"><svg width="18" height="18" viewBox="0 0 18 18"><path d="M7 11l4-4M8 4l2-2a3 3 0 0 1 4 4l-2 2M10 14l-2 2a3 3 0 0 1-4-4l2-2" fill="none" stroke="#fff" stroke-width="2"/></svg></div>
</article>

<aside class="sidebar">
  <div class="side-title" style="top:12px">CONTACT US</div>
  <div class="side-rule" style="top:42px"></div>
  <div class="field-label" style="top:58px">Your name</div>
  <div class="field" style="top:76px"></div>
  <div class="field-label" style="top:112px">Email *</div>
  <div class="field" style="top:130px"></div>
  <div class="field-label" style="top:166px">Message</div>
  <div class="field" style="top:184px;height:84px"></div>
  <div class="submit">SUBMIT</div>
  <div class="side-title" style="top:330px">MEET US</div>
  <div class="side-rule" style="top:360px"></div>
  <div class="person" style="top:380px">
    <div class="person-photo" role="img" aria-label="Portrait of sales representative"></div>
    <div class="person-name">Dana Whitfield</div>
    <div class="person-info">Mobile Phone: (555) 014-2281<br>Email: dana@prairiebio.com<br>Located in Omaha<br>Currently covering<br>NE, KS, IA, MO</div>
    <div class="person-social"><span></span><span></span><span></span></div>
  </div>
  <div class="person" style="top:530px">
    <div class="person-photo" role="img" aria-label="Portrait of sales representative"></div>
    <div class="person-name">Mark Ellison</div>
    <div class="person-info">Mobile Phone: (555) 017-4409<br>Email: mark@prairiebio.com<br>Located near Peoria<br>Currently covering<br>IL, WI, MN, MI, IN, OH</div>
    <div class="person-social"><span></span><span></span><span></span></div>
  </div>
</aside>

<section class="about">
  <div class="about-photo" role="img" aria-label="Close-up of braided steel hose weave"></div>
  <h2 class="section-title about-title">About us</h2>
  <p class="about-text">Prairie Biosolutions is a distribution channel, licensed partner and manufacturers representative group providing high quality fluid handling products and technical services to the regional biopharmaceutical community. With a core staff of experienced professionals and a team approach to all customers, we offer over 30 years of cGMP experience in the selection and use of most process consumable products. We're looking forward to working with you and sharing that experience in the selection and use of the products you rely on. We're looking forward to working with you!</p>
</section>

<footer class="site-footer">
  <div class="footer-title">CONTACT</div>
  <div class="footer-info">Mobile Phone: (555) 010-3370<br>Email: office@prairiebio.com<br>Located near Omaha<br>Currently covering<br>IL, WI, MN, MO, IA, KS, NE, ND, SD</div>
  <div class="to-top"><svg width="38" height="26" viewBox="0 0 38 26"><path d="M4 22 19 7l15 15" fill="none" stroke="#fff" stroke-width="7"/></svg></div>
  <div class="copyright">© Prairie Biosolutions, Corp.</div>
</footer>
<div class="footer-bar">
  <div class="footer-social"><span></span><span></span><span></span><span></span></div>
</div>

</body>
</html>
```